Storage Company Newsletter

We need a design for a newsletter for our company Vaultrix, a digital and physical asset storage company .The newsletter will be informative and educational covering tips on secure storage of personal documents and items both at home and at the work place. Rest easy with Vaultrix is our mantra. We have a pre-existing trademark & logo. Colors are blue and green. We can share the cmyk/rgb color information and background is grey.

Target Market(s)

Mass market – Middle to High income individuals

Industry/Entity Type

Digital

Font styles to use
Sans Serif

Colors
0393ce
00a88f
edf2f7

Requirements
Must have
• The newsletter linked to a CMS. In HTML5; Mail-chimp integration readable on Gmail, Yahoo, Hotmail and Outlook
Nice to have
• Sections of the newsletter are:
• Cover story
• News Flash
• Mwanachi Perspective
• Spotlight on the Counties
• CEO's Corner
• Tips and Helpful Information
• Important Dates and Events

```html
<!DOCTYPE html>
<html lang="en">
<head>
<meta charset="utf-8">
<title>Vaultrix Newsletter</title>
<link href="https://fonts.googleapis.com/css2?family=Arimo:wght@400;700&display=swap" rel="stylesheet">
<style>
  :root {
    --blue: #0393ce;
    --green: #00a88f;
    --green-dark: #007f68;
    --panel: #edf2f7;
    --ink: #444444;
    --ink-soft: #666666;
    --muted: #9a9a9a;
    --faint: #dddddd;
    --rule: #888888;
    --border: #dedede;
    --page: #ffffff;
  }
  * { box-sizing: border-box; margin: 0; padding: 0; }
  html, body { width: 723px; height: 1200px; overflow: hidden; background: var(--page); }
  body { font-family: "Arimo", Arial, sans-serif; color: var(--ink); }

  .newsletter { position: relative; width: 723px; height: 1200px; }
  .sheet { position: absolute; left: 3px; top: 8px; width: 716px; height: 1180px;
           box-shadow: 0 0 4px rgba(0,0,0,.25); background: var(--page); }

  .masthead { position: absolute; left: 12px; top: 20px; width: 697px; height: 146px;
              border: 1px solid #e6e6e6; border-bottom: none; }
  .brand { position: absolute; left: 76px; top: 58px; display: flex; align-items: center; gap: 10px; }
  .brand-mark { width: 30px; height: 30px; background: var(--blue); }
  .brand-name { font-size: 30px; font-weight: 700; color: var(--blue); }

  .issue-band { position: absolute; left: 12px; top: 165px; width: 697px; height: 27px;
                background: linear-gradient(90deg, #007e68 0%, #00a88f 45%, #007f68 100%);
                color: #fff; font-size: 12px; line-height: 27px; text-align: right; padding-right: 33px; }

  .lead { position: absolute; left: 12px; top: 192px; width: 697px; height: 162px; background: var(--panel);
          border-bottom: 1px solid #dfe4e9; }
  .section-title { font-weight: 400; color: var(--ink); letter-spacing: -0.5px; }
  .cover-story { position: absolute; left: 17px; top: 10px; width: 440px; }
  .cover-story .section-title { font-size: 30px; margin-bottom: 10px; }
  .cover-story p { font-size: 10.5px; line-height: 16px; color: var(--ink-soft); }
  .events { position: absolute; left: 483px; top: 14px; width: 200px; }
  .events .section-title { font-size: 21px; margin-bottom: 8px; }
  .events ul { list-style: none; }
  .events li { display: flex; gap: 10px; font-size: 10.5px; line-height: 13px; color: #111; margin-bottom: 15px; }
  .events svg { flex: none; margin-top: 0; }

  .tips { position: absolute; left: 12px; top: 372px; width: 697px; height: 213px; }
  .tip { position: absolute; top: 0; width: 202px; }
  .tip p { font-size: 10.5px; line-height: 16px; color: var(--muted); margin-top: 12px; }
  .photo { height: 80px; }
  .divider-v { position: absolute; top: 0; height: 213px; border-left: 1px dotted #999; }

  .rule { position: absolute; left: 12px; width: 697px; border-top: 1px solid var(--rule); }

  .ceo-corner { position: absolute; left: 21px; top: 619px; width: 680px; height: 111px; }
  .ceo-photo { position: absolute; left: 0; top: 0; width: 206px; height: 111px;
               background: linear-gradient(90deg, #a23d86 0%, #7a3f63 45%, #c9a89a 100%); border-radius: 2px; }
  .ceo-text { position: absolute; left: 221px; top: 2px; width: 450px; }
  .ceo-text .section-title { font-size: 30px; margin-bottom: 6px; }
  .ceo-text p { font-size: 10.5px; line-height: 16px; color: var(--ink-soft); }

  .feature { position: absolute; top: 777px; width: 220px; height: 223px; border: 1px solid var(--border); }
  .feature-head { height: 36px; background: linear-gradient(180deg, #00b195 0%, #007e66 100%);
                  color: #fff; font-weight: 700; font-size: 11.5px; display: flex; align-items: center;
                  gap: 10px; padding-left: 8px; margin: -1px -1px 0; box-shadow: 0 6px 6px -4px rgba(0,0,0,.3); }
  .feature p { font-size: 10.5px; line-height: 16px; color: var(--ink-soft); padding: 21px 12px 0; }

  .footer-line { position: absolute; left: 12px; top: 1023px; width: 697px; height: 4px; background: #edf1e6; }
  .subscribe { position: absolute; left: 14px; top: 1036px; font-size: 10.5px; color: var(--ink-soft); }
  .subscribe a { color: var(--green); text-decoration: none; }
  .social { position: absolute; right: 11px; top: 1034px; display: flex; gap: 7px; }
  .social span { width: 17px; height: 17px; background: var(--green); border-radius: 2px; }
  .legal { position: absolute; left: 14px; top: 1090px; width: 420px; font-size: 10px; line-height: 14px; color: var(--faint); }
  .legal p + p { margin-top: 2px; }
  .copyright { position: absolute; right: 11px; top: 1116px; font-size: 10.5px; color: var(--faint); }
</style>
</head>
<body>
<main class="newsletter">
  <div class="sheet">
    <header class="masthead">
      <div class="brand">
        <span class="brand-mark"></span>
        <span class="brand-name">Vaultrix</span>
      </div>
    </header>
    <div class="issue-band">// NEWSLETTER ARTICLE 1</div>

    <section class="lead">
      <div class="cover-story">
        <h2 class="section-title">cover story</h2>
        <p>Valuable documents include a wide range of items such as landtitle deeds, certificates, letters, photographs, newspaper cuttings andmemorabilia. The longevity of these items can be threatened by numerous factorssuch as light, moisture, insects such as silverfish, and physical damage.&nbsp; By taking these simple precautions outlinedbelow, you can preserve your valuable documents and keep them for posterity.</p>
      </div>
      <div class="events">
        <h2 class="section-title">important events</h2>
        <ul>
          <li><svg width="18" height="18" viewBox="0 0 18 18"><circle cx="9" cy="9" r="7.5" fill="none" stroke="var(--blue)" stroke-width="1.6"/><path d="M7 5.5 L12 9 L7 12.5 Z" fill="var(--blue)"/></svg>Lorem ipsum dolor sit amet, consectetur adipiscing elit.</li>
          <li><svg width="18" height="18" viewBox="0 0 18 18"><circle cx="9" cy="9" r="7.5" fill="none" stroke="var(--blue)" stroke-width="1.6"/><path d="M7 5.5 L12 9 L7 12.5 Z" fill="var(--blue)"/></svg>Lorem ipsum dolor sit amet, consectetur adipiscing elit.</li>
          <li><svg width="18" height="18" viewBox="0 0 18 18"><circle cx="9" cy="9" r="7.5" fill="none" stroke="var(--blue)" stroke-width="1.6"/><path d="M7 5.5 L12 9 L7 12.5 Z" fill="var(--blue)"/></svg>Lorem ipsum dolor sit amet, consectetur adipiscing elit.</li>
        </ul>
      </div>
    </section>

    <section class="tips">
      <article class="tip" style="left:9px">
        <div class="photo" role="img" aria-label="Colourful numbered file binders on a shelf" style="background:linear-gradient(90deg,#f3c9a8 0%,#c23a4a 35%,#d9b23a 65%,#f6e6c8 100%)"></div>
        <p>Valuabledocuments should be stored off the floor and away from external walls orwindows, to protect them from dramatic fluctuations in temperature andhumidity. Storage areas must remain dry to prevent mould growth and waterdamage.</p>
      </article>
      <span class="divider-v" style="left:227px"></span>
      <article class="tip" style="left:248px">
        <div class="photo" role="img" aria-label="Hand pressing buttons on an office copier" style="background:linear-gradient(135deg,#c9cdd6 0%,#8b7f82 40%,#d8e0ea 100%)"></div>
        <p>Valuabledocuments should be stored off the floor and away from external walls orwindows, to protect them from dramatic fluctuations in temperature andhumidity. Storage areas must remain dry to prevent mould growth and waterdamage.</p>
      </article>
      <span class="divider-v" style="left:468px"></span>
      <article class="tip" style="left:487px">
        <div class="photo" role="img" aria-label="Printed pages running through a press" style="background:linear-gradient(180deg,#5a6270 0%,#e3d3d6 55%,#c7b9c0 100%)"></div>
        <p>Valuabledocuments should be stored off the floor and away from external walls orwindows, to protect them from dramatic fluctuations in temperature andhumidity. Storage areas must remain dry to prevent mould growth and waterdamage.</p>
      </article>
    </section>

    <hr class="rule" style="top:598px">

    <section class="ceo-corner">
      <div class="ceo-photo" role="img" aria-label="Portrait of the chief executive"></div>
      <div class="ceo-text">
        <h2 class="section-title">ceo’s corner</h2>
        <p>As a public company, we are responsible for driving our business forward to the benefit of all our stakeholders and providing our stockholders with a return on their investment commensurate with our valuation as a premier industrial company. This will only be accomplished by our continued focus on quality, reliability, durability, vocational value and customer service.</p>
      </div>
    </section>

    <hr class="rule" style="top:748px">

    <article class="feature" style="left:12px">
      <h3 class="feature-head"><svg width="18" height="18" viewBox="0 0 18 18"><circle cx="9" cy="9" r="7.5" fill="none" stroke="var(--green-dark)" stroke-width="1.6"/><path d="M7 5.5 L12 9 L7 12.5 Z" fill="var(--green-dark)"/></svg>Mwanachi Perspective</h3>
      <p>Lorem Ipsum is simply dummy text of the printing and typesetting industry. Lorem Ipsum has been the industry’s standard dummy text ever since the 1500s, when an unknown printer took a galley of type and scrambled it to make a type specimen book.</p>
    </article>
    <article class="feature" style="left:252px">
      <h3 class="feature-head"><svg width="18" height="18" viewBox="0 0 18 18"><circle cx="9" cy="9" r="7.5" fill="none" stroke="var(--green-dark)" stroke-width="1.6"/><path d="M7 5.5 L12 9 L7 12.5 Z" fill="var(--green-dark)"/></svg>Spotlight on the Counties</h3>
      <p>Lorem Ipsum is simply dummy text of the printing and typesetting industry. Lorem Ipsum has been the industry’s standard dummy text ever since the 1500s, when an unknown printer took a galley of type and scrambled it to make a type specimen book.</p>
    </article>
    <article class="feature" style="left:490px">
      <h3 class="feature-head"><svg width="18" height="18" viewBox="0 0 18 18"><circle cx="9" cy="9" r="7.5" fill="none" stroke="var(--green-dark)" stroke-width="1.6"/><path d="M7 5.5 L12 9 L7 12.5 Z" fill="var(--green-dark)"/></svg>Helpful Information</h3>
      <p>Lorem Ipsum is simply dummy text of the printing and typesetting industry. Lorem Ipsum has been the industry’s standard dummy text ever since the 1500s, when an unknown printer took a galley of type and scrambled it to make a type specimen book.</p>
    </article>

    <footer>
      <div class="footer-line"></div>
      <p class="subscribe">Incase you haven’t subscribe our newsletter please <a href="#">click here to subscribe</a></p>
      <div class="social" aria-label="Social links"><span></span><span></span><span></span></div>
      <div class="legal">
        <p>You are currently subscribed to receive newsletter&nbsp; from valuable documents, we respects your privacy and does not share any information about you with other parties.</p>
        <p>You can unsubscribe from this email or modify your subscription settings at any time.</p>
      </div>
      <p class="copyright">© valuable documents,&nbsp; All Rights Reserved</p>
    </footer>
  </div>
</main>
</body>
</html>
```